Velmora Water Purification

We need a website set up on a "Free account" WordPress platform. (This is the type of Wordpress site that you can sign up for and create online for free (not a server-hosted type.)
The website will be for a water purification company. They install devices in homes to purify the water for safer drinking, bathing, and cleaning.
Our logo is attached. Please keep color scheme of the website consistent with the logo.
Water Purification

```html
<!DOCTYPE html>
<html lang="en">
<head>
<meta charset="utf-8">
<title>Velmora Water Purification</title>
<link href="https://fonts.googleapis.com/css2?family=Exo+2:wght@400;500;700;800&family=Roboto:wght@400;500;700&display=swap" rel="stylesheet">
<style>
:root{
  --brand-blue:#1f7fc6;
  --brand-cyan:#4ec6ea;
  --sky-light:#cfe9f8;
  --sky-mid:#8fc9ec;
  --button-blue:#2a93d1;
  --ink:#1c1c1c;
  --muted:#8a8a8a;
  --green:#1fa14b;
  --leaf:#7bc73a;
  --dark:#2e2e2e;
  --white:#ffffff;
}
*{margin:0;padding:0;box-sizing:border-box}
html,body{width:1200px;height:2811px;overflow:hidden;background:var(--white)}
body{position:relative;font-family:"Roboto",Arial,sans-serif;color:var(--ink)}
.abs{position:absolute}
.heading{font-family:"Exo 2",Arial,sans-serif;font-weight:500;letter-spacing:1px;text-align:center}
.btn{position:absolute;display:flex;align-items:center;justify-content:center;font-family:"Exo 2",Arial,sans-serif;font-weight:800;font-size:14px;letter-spacing:1.5px;color:var(--white)}
.btn-dark{background:#111}

/* header + hero */
.hero-band{left:0;top:0;width:1200px;height:640px;background:radial-gradient(ellipse at 15% 70%,var(--sky-mid),transparent 55%),radial-gradient(ellipse at 90% 30%,var(--sky-light),transparent 60%),linear-gradient(180deg,#f4fafe 0%,#e3f2fb 60%,#bfe2f6 100%)}
.brand{left:185px;top:52px;display:flex;align-items:center;gap:10px;font-family:"Exo 2",Arial,sans-serif;font-weight:700;font-size:22px;color:var(--brand-blue)}
.brand-dot{width:26px;height:26px;border-radius:50%;background:var(--brand-blue)}
.topline{top:20px;right:172px;display:flex;gap:36px;font-size:13px;color:#333;align-items:center}
.topline span{display:flex;align-items:center;gap:10px}
.nav{top:64px;right:172px;display:flex;gap:16px;font-size:14px;color:#222;letter-spacing:.3px}
.hero-photo{left:173px;top:145px;width:862px;height:435px;background:linear-gradient(180deg,#6fa7d8 0%,#a7cdea 45%,#4d7fb0 60%,#2a5a8e 100%)}
.hero-title{left:173px;width:1070px;top:305px;color:var(--white);font-family:"Exo 2",Arial,sans-serif;font-size:21px;letter-spacing:1px;line-height:24px;text-align:center;font-weight:500}
.hero-btn{left:630px;top:378px;width:151px;height:38px;background:var(--button-blue)}

/* features */
.features-title{left:0;width:1200px;top:712px;font-size:24px;color:var(--brand-blue)}
.feature{top:800px;width:240px;text-align:center}
.feature-icon{margin:0 auto;width:64px;height:64px}
.feature h3{margin-top:36px;font-family:"Exo 2",Arial,sans-serif;font-weight:500;font-size:14px;color:var(--brand-blue);letter-spacing:.8px}
.feature p{margin-top:22px;font-size:13.5px;line-height:18.5px;color:var(--muted)}

/* service */
.service-band{left:0;top:1105px;width:1200px;height:460px;background:radial-gradient(ellipse at 30% 50%,#c9ef8e,transparent 60%),radial-gradient(ellipse at 75% 60%,#a7de5a,transparent 55%),linear-gradient(160deg,var(--leaf) 0%,#9fd85a 40%,#5fb52c 100%)}
.service-title{left:0;width:1200px;top:1168px;font-size:23px;color:#111}
.service-item h3{font-family:"Exo 2",Arial,sans-serif;font-weight:500;font-size:23px;letter-spacing:1px;color:#111}
.service-item p{font-size:13.5px;line-height:16.5px;color:#111;margin-top:4px}
.know-btn{left:525px;top:1458px;width:151px;height:37px}

/* product */
.product-title{left:0;width:1200px;top:1634px;font-size:24px;color:#111}
.product-frame{top:1702px;width:391px;height:356px;border:1.5px solid var(--brand-cyan);display:flex;align-items:center;justify-content:center}
.product-photo{width:190px;height:290px;border-radius:60px 60px 24px 24px;background:linear-gradient(90deg,#5f6973 0%,#e9edf0 30%,#ffffff 55%,#c8ced3 80%,#4e5660 100%)}
.product-name{top:2090px;width:391px;text-align:center;font-family:"Exo 2",Arial,sans-serif;font-size:24px;color:var(--green);letter-spacing:.8px}
.product-list{top:2147px;width:330px;list-style:none;font-size:13px;line-height:15.5px;color:#222}
.product-list li{margin-bottom:14px;padding-left:12px;position:relative}
.product-list li::before{content:"";position:absolute;left:0;top:6px;width:4px;height:4px;border-radius:50%;background:#222}
.more-btn{left:525px;top:2361px;width:176px;height:37px}

/* footer */
.footer-map{left:0;top:2475px;width:565px;height:290px;background:linear-gradient(135deg,#c8def0 0%,#eef1e8 35%,#e6efdc 70%,#dbe9d2 100%)}
.footer-links{left:565px;top:2475px;width:225px;height:290px;background:var(--brand-cyan);color:var(--white)}
.footer-links::before{content:"";position:absolute;left:-14px;top:138px;border-top:14px solid transparent;border-bottom:14px solid transparent;border-right:14px solid var(--brand-cyan)}
.footer-contact{left:790px;top:2475px;width:410px;height:290px;background:var(--dark);color:var(--white)}
.footer-heading{font-family:"Exo 2",Arial,sans-serif;font-size:13px;letter-spacing:.6px}
.link-list{list-style:none;margin-top:20px;font-size:11px}
.link-list li{margin-bottom:11px;padding-left:9px;position:relative}
.link-list li::before{content:"";position:absolute;left:0;top:4px;border-top:3px solid transparent;border-bottom:3px solid transparent;border-left:4px solid var(--white)}
.contact-row{display:flex;gap:14px;font-size:10.5px;line-height:13px;color:#ddd;margin-top:14px}
.social{display:flex;gap:6px;margin-top:12px}
.social span{width:19px;height:19px;background:#777}
.copyright-bar{left:0;top:2765px;width:1200px;height:46px;background:var(--white);font-size:9px;color:#333;letter-spacing:.3px}
</style>
</head>
<body>

<header>
  <div class="abs hero-band"></div>
  <div class="abs brand"><span class="brand-dot"></span>Velmora Water Purification</div>
  <div class="abs topline">
    <span><svg width="14" height="14" viewBox="0 0 24 24"><path fill="#1f6fb5" d="M6.6 10.8c1.4 2.8 3.8 5.1 6.6 6.6l2.2-2.2c.3-.3.7-.4 1-.2 1.1.4 2.3.6 3.6.6.6 0 1 .4 1 1V20c0 .6-.4 1-1 1C10.6 21 3 13.4 3 4c0-.6.4-1 1-1h3.5c.6 0 1 .4 1 1 0 1.3.2 2.5.6 3.6.1.3 0 .7-.2 1z"/></svg>+1 555 0142 0198</span>
    <span><svg width="18" height="13" viewBox="0 0 18 13"><rect width="18" height="13" fill="#1f6fb5"/><path d="M0 0l9 7 9-7" fill="none" stroke="#fff" stroke-width="1.4"/></svg>info@velmorawater.com</span>
  </div>
  <nav class="abs nav"><span>HOME</span><span>COMPANY</span><span>TECHNOLOGIES</span><span>APPLICATIONS</span><span>CONTACT US</span></nav>

  <div class="abs hero-photo" role="img" aria-label="Glass being filled with clear water beside a calm lake under a blue sky"></div>
  <h1 class="abs hero-title" style="left:173px;width:1070px;">OUR TECHNOLOGIES DELIVER<br>ENVIRONMENTAL &amp; ECONOMICAL BENEFITS</h1>
  <div class="btn hero-btn">BOOK A DEMO</div>
</header>

<section>
  <h2 class="abs heading features-title">OUR KEY FEATURES</h2>
  <div class="abs feature" style="left:180px">
    <div class="feature-icon" role="img" aria-label="Water drop with a globe" style="border-radius:50%;background:radial-gradient(circle at 40% 40%,#7fd0f2,#2a8fd0 70%,#6ab43a 100%)"></div>
    <h3>ENVIRONMENTAL FRIENDLY</h3>
    <p>Sed gravida, justo efficitur sollicitu-din egestas, diam tellus vehicula sem, in blandit nisi magna vitae risus. Maecenas at feugiat enim. Ut quam enim, convallis eget enim non, tincidunt congue neque.</p>
  </div>
  <div class="abs feature" style="left:457px">
    <div class="feature-icon" role="img" aria-label="Coin plant in a pot" style="border-radius:50%;background:radial-gradient(circle at 50% 30%,#2fae4e 0 35%,#a0522d 36% 70%,transparent 71%)"></div>
    <h3>AFFORDABLE</h3>
    <p>Sed gravida, justo efficitur sollicitu-din egestas, diam tellus vehicula sem, in blandit nisi magna vitae risus. Maecenas at feugiat enim. Ut quam enim, convallis eget enim non, tincidunt congue neque.</p>
  </div>
  <div class="abs feature" style="left:712px">
    <svg class="feature-icon" viewBox="0 0 64 64"><path d="M32 12C26 24 21 30 21 38a11 11 0 0 0 22 0c0-8-5-14-11-26z" fill="#2a8fd0"/><path d="M27 37a5 5 0 0 0 4 6" fill="none" stroke="#bfe6fa" stroke-width="2"/></svg>
    <h3>CONSISTENT</h3>
    <p>Sed gravida, justo efficitur sollicitu-din egestas, diam tellus vehicula sem, in blandit nisi magna vitae risus. Maecenas at feugiat enim. Ut quam enim, convallis eget enim non, tincidunt congue neque.</p>
  </div>
</section>

<section>
  <div class="abs service-band" role="img" aria-label="Clear stream flowing over bright green moss"></div>
  <h2 class="abs heading service-title">OUR SERVICE</h2>

  <svg class="abs" style="left:193px;top:1312px" width="74" height="62" viewBox="0 0 74 62" fill="none" stroke="#111" stroke-width="2">
    <path d="M12 38l3 7 7 1-5 5 1 7-6-3-6 3 1-7-5-5 7-1z"/>
    <path d="M32 30l3 6 7 1-5 5 1 6-6-3-6 3 1-6-5-5 7-1z"/>
    <path d="M55 4l3 6 6 1-4 4 1 6-6-3-5 3 1-6-4-4 6-1z"/>
    <path d="M48 24l2 5 5 1-4 3 1 5-4-2-5 2 1-5-4-3 5-1z"/>
    <path d="M28 8l2 4 4 1-3 3 1 4-4-2-4 2 1-4-3-3 4-1z"/>
  </svg>
  <div class="abs service-item" style="left:280px;top:1272px;width:300px">
    <h3>SPARKLING</h3>
    <p>Suspendisse vitae fringilla justo, in molestie ex. Pellentesque tempus aliquam justo, id luctus libero ullamcorper id. Suspendisse vitae fringilla justo, in molestie ex. Pellentesque tempus aliquam justo, id luctus libero ullamcorper id.</p>
  </div>

  <svg class="abs" style="left:615px;top:1308px" width="66" height="66" viewBox="0 0 66 66" fill="none" stroke="#111" stroke-width="2.5" stroke-linecap="round">
    <path d="M33 4v58M8 18l50 30M8 48l50-30"/>
    <path d="M26 8l7 7 7-7M26 58l7-7 7 7M7 26l10 3-3 9M59 40l-10-3 3-9M7 40l10-3-3-9M59 26l-10 3 3 9"/>
  </svg>
  <div class="abs service-item" style="left:700px;top:1257px;width:325px">
    <h3>CHILLED</h3>
    <p>Suspendisse vitae fringilla justo, in molestie ex. Pellentesque tempus aliquam justo, id luctus libero ullamcorper id. Suspendisse vitae fringilla justo, in molestie ex. Pellentesque tempus aliquam justo, id luctus libero ullamcorper id.</p>
  </div>

  <div class="btn btn-dark know-btn">KNOW MORE</div>
</section>

<section>
  <h2 class="abs heading product-title">OUR PRODUCT</h2>
  <div class="abs product-frame" style="left:201px"><div class="product-photo" role="img" aria-label="White countertop water purifier"></div></div>
  <div class="abs product-frame" style="left:621px"><div class="product-photo" role="img" aria-label="White countertop water purifier"></div></div>

  <h3 class="abs product-name" style="left:201px">WATER PURIFIERS</h3>
  <h3 class="abs product-name" style="left:621px">WATER PURIFIERS</h3>

  <ul class="abs product-list" style="left:230px">
    <li>Suspendisse vitae fringilla justo, in molestie ex.</li>
    <li>Pellentesque tempus aliquam justo, id luctus libero ullamcorper id.</li>
    <li>Suspendisse vitae fringilla justo, in molestie ex.</li>
    <li>Pellentesque tempus aliquam justo, id luctus libero ullamcorper id.</li>
  </ul>
  <ul class="abs product-list" style="left:650px">
    <li>Suspendisse vitae fringilla justo, in molestie ex.</li>
    <li>Pellentesque tempus aliquam justo, id luctus libero ullamcorper id.</li>
    <li>Suspendisse vitae fringilla justo, in molestie ex.</li>
    <li>Pellentesque tempus aliquam justo, id luctus libero ullamcorper id.</li>
  </ul>

  <div class="btn btn-dark more-btn">MORE PRODUCTS</div>
</section>

<footer>
  <div class="abs footer-map" role="img" aria-label="Road map of the service region"></div>
  <div class="abs footer-links">
    <div style="position:absolute;left:26px;top:52px">
      <div class="footer-heading">USE FULL LINKS</div>
      <ul class="link-list"><li>Home</li><li>Company</li><li>Technologies</li><li>Applications</li><li>Contact Us</li></ul>
    </div>
  </div>
  <div class="abs footer-contact">
    <div style="position:absolute;left:24px;top:48px;width:350px">
      <div class="footer-heading">CONTACT INFO</div>
      <div class="contact-row" style="margin-top:16px"><svg width="11" height="11" viewBox="0 0 12 12"><path d="M6 1L1 6h2v5h6V6h2z" fill="#aaa"/></svg><span>1st Floor, 114<br>Address line 2<br>State, country</span></div>
      <div class="contact-row" style="margin-top:20px"><svg width="11" height="11" viewBox="0 0 24 24"><path fill="#aaa" d="M6.6 10.8c1.4 2.8 3.8 5.1 6.6 6.6l2.2-2.2c.3-.3.7-.4 1-.2 1.1.4 2.3.6 3.6.6.6 0 1 .4 1 1V20c0 .6-.4 1-1 1C10.6 21 3 13.4 3 4c0-.6.4-1 1-1h3.5c.6 0 1 .4 1 1 0 1.3.2 2.5.6 3.6.1.3 0 .7-.2 1z"/></svg><span>Telephone: +1 555 0142 0198</span></div>
      <div class="contact-row" style="margin-top:10px"><svg width="11" height="9" viewBox="0 0 18 13"><rect width="18" height="13" fill="#aaa"/><path d="M0 0l9 7 9-7" fill="none" stroke="#2e2e2e" stroke-width="1.6"/></svg><span>Email: info@velmorawater.com</span></div>
      <div class="footer-heading" style="margin-top:24px">CONNECT WITH US</div>
      <div class="social"><span></span><span></span><span></span></div>
    </div>
  </div>
  <div class="abs copyright-bar">
    <span class="abs" style="left:138px;top:20px">COPYRIGHT VELMORA WATER PURIFICATION 2017</span>
    <span class="abs" style="left:739px;top:20px">HOME &nbsp;|&nbsp; WEBSITE COPYRIGHT DETAILS &nbsp;|&nbsp; TERMS &amp; POLICIES &nbsp;|&nbsp; CONTACT</span>
  </div>
</footer>

</body>
</html>
```